Puslishing House Needs poster Design for Medical Book

We need an advertisement desing for a medical book on cardiology named "Lumivarte" (Hypertension), which 2nd Edition we launched last August. What makes this book special is that this is the first time in history that a hypertension book has a second edition in Brazil and was written by the Vessel Studies Unit of the Austral Guild of Circulatory Medicine in comemoration in its 100 years. The two news about this book is that we sold 1000 units since we launched (which is good) and we have now an ebook version for all tablet, smartphones and readers. From this month on it is going to happen importants hypertension meetings and we want to promote this two news about this book - 1000 units sold and ebook version. We would like to see designs that use orange (the publishing house color) and communicate celebration.

Target Market(s)

Doctors Specialist from several segments like Cardiology, Endocrinology, Nephrology, Nutrition. Most of the target are man with 50 years-old.

Industry/Entity Type

Medical

Requirements
Must have
• The adverstisement must have the attached book cover and publishing house logo (Quorvane) using only the name (without the tree) or the complete logo.
Should not have
• The design should not use old-style, serif fonts like Times new Roman.

```html
<!DOCTYPE html>
<html lang="en">
<head>
<meta charset="utf-8">
<title>Lumivarte – 1000 Units Sold and E-Book Version</title>
<link rel="stylesheet" href="https://fonts.googleapis.com/css2?family=Rubik+Dirt&family=Montserrat:wght@400;600;700;800&family=Oswald:wght@500;600&display=swap">
<style>
  :root {
    --orange-deep: #ee6a12;
    --orange-mid: #f7871e;
    --orange-light: #fba23a;
    --gold-light: #f6d27a;
    --gold-deep: #c8921e;
    --white: #ffffff;
    --cover-green: #1e5a48;
    --cover-green-mid: #5e8e7c;
    --cover-pale: #f1f4f2;
    --title-red: #e8443a;
    --ink-dark: #2b2b2b;
    --brand-orange: #e8781c;
    --brand-navy: #1d3c78;
    --brand-red: #d6262e;
    --strip: #f07a1a;
  }
  * { box-sizing: border-box; margin: 0; padding: 0; }
  html, body { width: 837px; height: 1200px; overflow: hidden; }
  body { background: var(--orange-mid); font-family: "Montserrat", sans-serif; }

  .poster {
    position: relative;
    width: 837px;
    height: 1200px;
    overflow: hidden;
    background: radial-gradient(ellipse 70% 55% at 50% 38%, var(--orange-light) 0%, var(--orange-mid) 45%, var(--orange-deep) 100%);
  }

  .gift-ribbon {
    position: absolute;
    top: 0; right: 0;
    width: 340px; height: 350px;
    background: radial-gradient(ellipse 60% 55% at 62% 32%, var(--gold-light) 0%, var(--gold-deep) 45%, rgba(200,146,30,0) 75%);
  }

  .headline { position: absolute; left: 0; width: 100%; text-align: center; color: var(--white); }
  .headline-units {
    top: 192px;
    font-family: "Rubik Dirt", sans-serif;
    font-size: 92px;
    letter-spacing: 1px;
    line-height: 1;
  }
  .headline-sold {
    top: 282px;
    font-size: 76px;
    line-height: 1;
    letter-spacing: -1px;
  }
  .headline-sold .strong { font-weight: 800; }
  .headline-sold .light { font-weight: 400; }
  .headline-ebook {
    top: 362px;
    font-size: 45px;
    font-weight: 700;
    line-height: 1;
  }

  .book-cover {
    position: absolute;
    left: 195px; top: 423px;
    width: 426px; height: 569px;
    overflow: hidden;
    box-shadow: 0 4px 14px rgba(120,50,0,0.35);
  }
  .cover-art {
    position: absolute; inset: 0;
    background: linear-gradient(180deg, var(--cover-green) 0%, var(--cover-green-mid) 30%, #c9d8d2 48%, var(--cover-pale) 60%, var(--cover-pale) 100%);
  }
  .cover-authors {
    position: absolute;
    left: 288px; top: 60px;
    font-family: "Oswald", sans-serif;
    font-weight: 600;
    font-size: 19px;
    line-height: 33px;
    color: var(--white);
  }
  .cover-title {
    position: absolute;
    left: 0; width: 100%;
    top: 218px;
    text-align: center;
    font-family: "Oswald", sans-serif;
    font-weight: 500;
    font-size: 70px;
    letter-spacing: 1px;
    color: var(--title-red);
    line-height: 1;
  }
  .cover-publisher {
    position: absolute;
    left: 18px; bottom: 40px;
    font-weight: 700;
    font-size: 10px;
    color: var(--ink-dark);
  }
  .cover-edition {
    position: absolute;
    left: 84px; bottom: 24px;
    font-size: 12px;
    font-weight: 600;
    color: var(--ink-dark);
  }
  .cover-unit {
    position: absolute;
    left: 240px; bottom: 20px;
    display: flex; align-items: center; gap: 6px;
  }
  .cover-unit .seal {
    width: 24px; height: 24px; border-radius: 50%;
    background: #3d6aa8;
  }
  .cover-unit .unit-name {
    font-size: 7px; font-weight: 700; line-height: 1.2;
    color: var(--ink-dark); width: 140px;
  }

  .partner-band {
    position: absolute;
    left: 0; top: 1034px;
    width: 100%; height: 136px;
    background: var(--white);
    display: flex; align-items: center; justify-content: space-around;
    padding: 0 40px;
  }
  .partner-strip {
    position: absolute; left: 0; top: 1170px;
    width: 100%; height: 30px;
    background: var(--strip);
  }
  .partner { display: flex; align-items: center; gap: 8px; font-weight: 700; }
  .partner-quorvane { color: var(--brand-orange); font-size: 22px; }
  .partner-vantaro { color: var(--ink-dark); font-size: 22px; letter-spacing: 2px; }
  .partner-brisello { color: var(--ink-dark); font-size: 26px; }
  .partner-brisello .mark { width: 22px; height: 22px; background: var(--ink-dark); }
  .partner-solmar { color: var(--brand-navy); font-size: 22px; }
</style>
</head>
<body>
<main class="poster">
  <div class="gift-ribbon" role="img" aria-label="Golden gift ribbon and bow wrapped over the top right corner"></div>

  <h1 class="headline headline-units">1000 UNITS</h1>
  <p class="headline headline-sold"><span class="strong">SOLD</span> <span class="light">AND</span></p>
  <p class="headline headline-ebook">E - BOOK VERSION</p>

  <section class="book-cover" aria-label="Lumivarte book cover, 2nd edition">
    <div class="cover-art" role="img" aria-label="Book cover artwork: green ink splash above a blood pressure gauge and inflation bulb"></div>
    <div class="cover-authors">
      <p>Marina C. Duarte</p>
      <p>Rafael Tessier</p>
      <p>Otávio Linhares</p>
    </div>
    <h2 class="cover-title">LUMIVARTE</h2>
    <p class="cover-publisher">QUORVANE</p>
    <p class="cover-edition">2ª EDIÇÃO</p>
    <div class="cover-unit">
      <span class="seal"></span>
      <span class="unit-name">VESSEL STUDIES UNIT<br>AUSTRAL GUILD OF CIRCULATORY MEDICINE</span>
    </div>
  </section>

  <footer class="partner-band">
    <span class="partner partner-quorvane">QUORVANE</span>
    <span class="partner partner-vantaro">VANTARO EDITORA</span>
    <span class="partner partner-brisello"><span class="mark"></span>Brisello</span>
    <span class="partner partner-solmar">EDITORA SOLMAR</span>
  </footer>
  <div class="partner-strip"></div>
</main>
</body>
</html>
```